Zelphone/Zelpad App Developer Showcase Website (Redesign)

We need an attractive, modern and professional looking re-design of an existing website: www.velkrimo.com.

We have a new logo and want the website to use this - although the colors used in the logo could be altered to suit the website color scheme.

This site should consist of
- a main page showing off a few sample of apps
- a separate page for each app (one page template suitable for all apps)
- a few subsidiary pages which can be based on a single similar template, such as an About page, and Help pages for some of the apps

Note - some of the apps are Zelphone only, and others are Zelpad only or for both. Hence the design should allow for showing off both.

There is no need for the design to allow for lots of app screenshots (there will be links to the wareshelf where more screenshot can be seen).

It is not necessary to optimise the design just for Zelphone screen viewing, but the
website should at least be reasonably usable on an Zelphone and Zelpad, as many users may be accessing the site from those devices.

Here are a few sites of similar developers - just for ideas. The first one listed is the one I think is the most attractive design. The main difference needed is that the primary function of this site is to show off the quality of the apps to app buyers, rather than to promote ourselves as app developers, which is only a secondary aim.

http://www.trelbworks.com.au/mobilebuilds.html
http://www.quendix.com.au/
http://www.parvolent.com/

Note - app screenshots and Zelphone and Zelpad device graphics templates (including glassy shadowed versions) are attached in a zip file.

Thank-you for all your submissions - your efforts are much appreciated. :-)

Seeing all the proposed designs has allowed me to see where I perhaps haven't been very clear in my brief, and also has helped me work out what type of design elements I prefer. So following is a refinement of the requirement.

The site requires only a simple layout ie.
At most it needs
- A Home page showing off a few screenshots, or with a scrolling/dynamic element, and a single link to veLKRM in the wareshelf
- An About Us page
- A Contact Us page (with email form for two types are enquires a) App Support Enquiry b) Business Enquiry
- A Page for each app, including 
  > some phone/screenshot graphics
  > a description of the app features
  > a link to buy the app in the wareshelf
  > a Viewtrove video demo link (for some apps only)
  > a link to a Help/FAQ page (for some apps only)

Note - if your design can show all the app info within the main page (eg. in a scrolling frame of some kind), then separate pages for each app might not even be required.

Things that are not needed are
- Request a Quote
- Follow us via Chatterleaf, Blipwire etc...

Regarding the graphical design elements, I have decided that I do prefer
- designs with lighter colored backgrounds, so not black or very dark designs
- designs that keep the orange/black colors in the velkrimo logo, and use colors which work well with these

I will now contact some of you individually with specific feedback where I can - but there are so many designs already that I may not be able to contact everyone. If not, please do review your design in light of the above comments to see how well it fits.

Thanks again, and I am very pleased with results so far!

Target Market(s)

1. Zelphone/Zelpad owners looking for useful apps - tech savvy, well-educated
2. Companies/people looking for experienced/expert ZOS development company

Requirements
Must have
• Expandable to allow new page to be added for each future apps

Use the attached new company logo design (although colors may be altered to suit website color scheme)

Site must be maintainable/expandable by ourselves once initial site is in place.
Nice to have
• Website nicely viewable from Zelphone browser

Would be nice to have some dynamic elements eg. scrolling showcase of different app screens on main page

```html
<!DOCTYPE html>
<html lang="en">
<head>
<meta charset="utf-8">
<title>velkrimo — Zelphone &amp; Zelpad Apps</title>
<link href="https://fonts.googleapis.com/css2?family=Arimo:wght@400;700&display=swap" rel="stylesheet">
<style>
:root{
  --orange:#f39a12;
  --orange-deep:#c8420c;
  --orange-mid:#e2611a;
  --ink:#2b2b2b;
  --grey:#7b7b7b;
  --grey-light:#a9a9a9;
  --line:#dcdcdc;
  --paper:#ffffff;
  --band:#f3f3f3;
}
*{margin:0;padding:0;box-sizing:border-box}
html,body{width:1200px;height:1168px;overflow:hidden}
body{font-family:"Arimo",Arial,sans-serif;background:var(--paper);color:var(--ink);position:relative}
.abs{position:absolute}

.site-header{position:absolute;left:0;top:0;width:1200px;height:110px;background:linear-gradient(#ffffff,#eeeeee)}
.brand{position:absolute;left:80px;top:34px;display:flex;align-items:center;gap:12px;font-size:44px;font-weight:700;color:var(--ink);letter-spacing:-1px}
.brand-dot{width:22px;height:22px;border-radius:50%;background:var(--orange)}
.main-nav a{position:absolute;top:45px;height:30px;line-height:30px;font-size:15px;color:var(--grey);text-decoration:none;text-align:center}
.main-nav .active{left:753px;width:78px;background:var(--orange);color:#fff;border-radius:3px;font-weight:700}

.hero{position:absolute;left:0;top:110px;width:1200px;height:471px;background:radial-gradient(ellipse at 45% 40%,#f07a22 0%,var(--orange-mid) 40%,var(--orange-deep) 100%)}
.hero-title{position:absolute;left:54px;top:70px;width:560px;font-size:38px;line-height:46px;font-weight:700;color:#fff;text-transform:uppercase}
.hero-text{position:absolute;left:56px;top:186px;width:560px;font-size:14px;line-height:29px;color:#fff}
.learn-more{position:absolute;left:107px;top:328px;width:233px;height:54px;background:linear-gradient(#ffffff,#e4e4e4);border-radius:4px;box-shadow:0 3px 6px rgba(0,0,0,.3);font-size:22px;color:#444;line-height:54px;padding-left:28px}
.learn-more i{position:absolute;right:14px;top:12px;width:30px;height:30px;border-radius:50%;background:var(--orange)}
.learn-more i::after{content:"";position:absolute;left:12px;top:9px;border-left:8px solid #fff;border-top:6px solid transparent;border-bottom:6px solid transparent}
.slider-dots span{position:absolute;top:437px;width:8px;height:8px;border-radius:50%;background:#fff}
.slider-dots .on{width:18px;height:18px;top:432px;background:none;border:3px solid #fff}
.device-art{position:absolute;left:590px;top:188px;width:545px;height:455px;border-radius:26px;background:linear-gradient(160deg,#2e2e2e,#6b7a88 55%,#1d1d1d)}

.section-title{position:absolute;left:114px;top:622px;font-size:21px;color:var(--grey)}
.arrow{position:absolute;top:760px;width:0;height:0;border-top:14px solid transparent;border-bottom:14px solid transparent}
.arrow.prev{left:70px;border-right:18px solid var(--orange)}
.arrow.next{left:1100px;border-left:18px solid #cfcfcf}
.app-card{position:absolute;top:697px;width:143px}
.app-shot{width:143px;height:170px;border:3px solid #e6e6e6;background:linear-gradient(#3a5a86,#7f9ec4)}
.app-name{margin-top:12px;font-size:17px;color:var(--ink)}
.app-type{margin-top:8px;font-size:13px;color:var(--grey)}

.footer-top{position:absolute;left:0;top:957px;width:1200px;height:143px;background:linear-gradient(#ffffff,#f7f7f7)}
.divider{position:absolute;top:975px;width:1px;height:110px;background:var(--line)}
.col-title{position:absolute;top:972px;font-size:16px;color:#555;text-transform:uppercase}
.quote{position:absolute;left:111px;top:1011px;width:320px;font-size:14px;line-height:20px;color:#555}
.author{position:absolute;left:300px;top:1066px;font-size:14px;font-weight:700;color:#444}
.email{position:absolute;left:506px;top:1014px;width:218px;height:27px;border:1px solid #ccc;background:#fff;font-size:13px;color:#999;padding:5px 8px}
.go{position:absolute;left:724px;top:1014px;width:59px;height:27px;background:var(--orange);color:#fff;font-weight:700;font-size:13px;text-align:center;line-height:27px}
.radio{position:absolute;top:1052px;font-size:13px;color:#666}
.radio::before{content:"";display:inline-block;width:11px;height:11px;border:1px solid #aaa;border-radius:50%;margin-right:7px;vertical-align:-1px}
.social{position:absolute;top:1016px;width:40px;height:40px}

.site-footer{position:absolute;left:0;top:1100px;width:1200px;height:68px;background:var(--band)}
.foot-links{position:absolute;left:68px;top:14px;font-size:12px;color:var(--grey-light)}
.foot-links span{margin:0 10px}
.copy{position:absolute;left:68px;top:40px;font-size:12px;color:var(--grey-light);letter-spacing:.5px}
.card{position:absolute;top:14px;width:36px;height:20px;border-radius:3px}
</style>
</head>
<body>
<header class="site-header">
  <div class="brand"><span>velkrimo</span><span class="brand-dot"></span></div>
  <nav class="main-nav">
    <a class="active" href="#">HOME</a>
    <a href="#" style="left:866px;width:60px">APPS</a>
    <a href="#" style="left:954px;width:60px">ABOUT</a>
    <a href="#" style="left:1058px;width:70px">CONTACT</a>
  </nav>
</header>

<section class="hero">
  <h1 class="hero-title">Lorem ipsum dolor sit amet, consectetuer</h1>
  <p class="hero-text">Lorem ipsum dolor sit amet, consectetuer adipiscing elit. Aenean commodo ligula eget dolor. Aenean massa. Cum sociis natoque penatibus et magnis dis parturient montes, nascetur ridiculus mus. Donec quam felis, ultricies nec,</p>
  <a class="learn-more">LEARN&nbsp; MORE<i></i></a>
  <div class="slider-dots"><span style="left:103px"></span><span style="left:125px"></span><span class="on" style="left:145px"></span></div>
</section>
<div class="device-art" role="img" aria-label="Zelpad and Zelphone devices showing the weather app"></div>

<h2 class="section-title">Screenshoots&nbsp; [ Zelphone&nbsp; |&nbsp; Zelpad ]</h2>
<span class="arrow prev"></span><span class="arrow next"></span>

<div class="app-card" style="left:114px"><div class="app-shot" role="img" aria-label="App screenshot: city weather list"></div><p class="app-name">Kiro Weather</p><p class="app-type">Type: Zelphone / Zelpad</p></div>
<div class="app-card" style="left:279px"><div class="app-shot" role="img" aria-label="App screenshot: rain radar map" style="background:linear-gradient(#cdd9e4,#93b0c8)"></div><p class="app-name">Kiro Weather</p><p class="app-type">Type: Zelphone / Zelpad</p></div>
<div class="app-card" style="left:443px"><div class="app-shot" role="img" aria-label="App screenshot: wind viewer dial" style="background:linear-gradient(#1b2a36,#3f7f98)"></div><p class="app-name">Kiro Weather</p><p class="app-type">Type: Zelphone / Zelpad</p></div>
<div class="app-card" style="left:608px"><div class="app-shot" role="img" aria-label="App screenshot: locations list" style="background:linear-gradient(#1e2a38,#2f4a62)"></div><p class="app-name">Kiro Weather</p><p class="app-type">Type: Zelphone / Zelpad</p></div>
<div class="app-card" style="left:774px"><div class="app-shot" role="img" aria-label="App screenshot: radar sweep" style="background:linear-gradient(#6b2e6e,#4a6a3a)"></div><p class="app-name">Kiro Weather</p><p class="app-type">Type: Zelphone / Zelpad</p></div>
<div class="app-card" style="left:939px"><div class="app-shot" role="img" aria-label="App screenshot: saved locations" style="background:linear-gradient(#2f4f7a,#d98a3a)"></div><p class="app-name">Kiro Weather</p><p class="app-type">Type: Zelphone / Zelpad</p></div>

<div class="footer-top"></div>
<span class="divider" style="left:424px"></span><span class="divider" style="left:862px"></span>
<h3 class="col-title" style="left:111px">Testimonials</h3>
<p class="quote">Lorem ipsum dolor sit amet, consectetuer adipiscing e penatibus et magnis</p>
<p class="author">- MARA TOLVEN</p>
<h3 class="col-title" style="left:506px">Newsletter</h3>
<div class="email">Enter Your E-mail</div><div class="go">GO</div>
<span class="radio" style="left:506px">Subscribe</span><span class="radio" style="left:605px">Unsubscribe</span>
<h3 class="col-title" style="left:912px">Follow us on</h3>
<svg class="social" style="left:912px" viewBox="0 0 40 40" role="img" aria-label="Feed"><rect width="40" height="40" rx="7" fill="#f39a12"/></svg>
<svg class="social" style="left:967px" viewBox="0 0 40 40" role="img" aria-label="Chatterleaf"><rect width="40" height="40" rx="7" fill="#3b5a98"/></svg>
<svg class="social" style="left:1024px;width:46px;height:46px;top:1012px" viewBox="0 0 46 46" role="img" aria-label="Blipwire"><circle cx="23" cy="23" r="21" fill="#3fb4e0"/></svg>

<footer class="site-footer">
  <p class="foot-links">Home<span>|</span>Services<span>|</span>About<span>|</span>Contact</p>
  <p class="copy">Copyright 2010 All rights reserved.</p>
  <span class="card" style="left:987px;background:#1a3d8f"></span>
  <span class="card" style="left:1030px;background:#e08a1e"></span>
  <span class="card" style="left:1073px;background:#4a8fce"></span>
</footer>
</body>
</html>
```